Legal Service Estimated Retainer and Average Case Value

We need an 11x14 flyer that contains the standard retainers and average cost be case, both provided in documents, for each case type we handle. We need the information displayed, preferably in a way that makes the information readable but less troubling to a client shocked at price of litigation. We need one sheet with the retainers and average case value merged into one table.

Target Market(s)

Potential Clients

Font styles to use
Serif
Sans Serif

```html
<!DOCTYPE html>
<html lang="en">
<head>
<meta charset="utf-8">
<title>Legal Service Estimated Retainer &amp; Average Case Value</title>
<link rel="stylesheet" href="https://fonts.googleapis.com/css2?family=Cinzel:wght@400;500&family=Source+Sans+3:wght@400;500&display=swap">
<style>
  :root {
    --page-bg: #e6e7ea;
    --navy-deep: #12174a;
    --navy-mid: #1f2f7c;
    --royal: #1b4a9e;
    --royal-bright: #2152ad;
    --label-blue: #1f3f9a;
    --row-light: #f3f3f4;
    --row-mid: #e5eaf2;
    --rule: #d4d7dd;
    --muted-text: #555a63;
    --white: #ffffff;
  }
  * { box-sizing: border-box; margin: 0; padding: 0; }
  html, body { width: 1087px; height: 1200px; overflow: hidden; }
  body { background: var(--page-bg); position: relative; }

  .flyer {
    position: absolute;
    left: 88px; top: 20px;
    width: 792px; height: 1008px;
    transform: scale(1.151);
    transform-origin: top left;
    background: linear-gradient(180deg, #ffffff 0%, #f6f7fa 60%, #e4e7ef 100%);
    overflow: hidden;
  }

  .masthead {
    position: absolute; left: 0; top: 0; width: 792px; height: 210px;
    background: radial-gradient(ellipse 420px 260px at 360px 70px, #25368c 0%, var(--navy-mid) 35%, var(--navy-deep) 100%);
  }
  .masthead-strip {
    position: absolute; left: 0; top: 210px; width: 792px; height: 13px;
    background: var(--royal);
  }
  .firm-name {
    position: absolute; left: 50px; top: 108px;
    display: flex; align-items: center; gap: 10px;
    font-family: 'Cinzel', serif; font-weight: 400;
    font-size: 17px; letter-spacing: 0.5px; color: var(--white);
  }
  .firm-mark { width: 12px; height: 12px; background: var(--white); }
  .flyer-title {
    position: absolute; right: 43px; top: 72px;
    text-align: right;
    font-family: 'Cinzel', serif; font-weight: 400;
    font-size: 25px; line-height: 31px; letter-spacing: 0.6px;
    color: var(--white);
  }

  .fee-table {
    position: absolute; left: 48px; top: 281px; width: 701px;
    box-shadow: 0 2px 4px rgba(0,0,0,0.12);
  }
  .fee-head { display: grid; grid-template-columns: 548px 153px; height: 51px; }
  .fee-head-main {
    background: linear-gradient(180deg, var(--royal-bright), #163f8f);
    border-radius: 6px 0 0 0;
    font-family: 'Cinzel', serif; font-size: 19px; letter-spacing: 0.7px;
    color: var(--white); padding: 14px 0 0 15px;
  }
  .fee-head-avg {
    background: var(--royal); border-radius: 0 6px 0 0;
    border-left: 1px solid #5577c0;
    font-family: 'Cinzel', serif; font-size: 14px; line-height: 16px;
    color: #d8e1f4; text-align: center; padding-top: 10px;
  }
  .fee-row { display: grid; grid-template-columns: 402px 146px 153px; height: 42px; }
  .fee-row + .fee-row .case-type,
  .fee-row + .fee-row .retainer { border-top: 1px solid var(--rule); }
  .fee-row + .fee-row .avg-fee { border-top: 1px solid #5777be; }
  .case-type {
    background: var(--row-light);
    font-family: 'Source Sans 3', sans-serif; font-size: 14px;
    color: var(--label-blue); padding: 14px 0 0 14px;
  }
  .retainer {
    background: var(--row-mid); border-left: 1px solid var(--rule);
    font-family: 'Source Sans 3', sans-serif; font-size: 14px;
    color: var(--muted-text); padding: 14px 0 0 50px; line-height: 14px;
  }
  .avg-fee {
    background: var(--royal);
    font-family: 'Source Sans 3', sans-serif; font-size: 14px;
    color: var(--white); padding: 14px 0 0 28px;
  }

  .footer-band { position: absolute; left: 0; top: 978px; width: 792px; height: 30px; }
</style>
</head>
<body>
  <main class="flyer">
    <header class="masthead">
      <div class="firm-name"><span class="firm-mark"></span>Marcus D Whitfield</div>
      <h1 class="flyer-title">Legal Service<br>Estimated Retainer &amp;<br>Average Case Value</h1>
    </header>
    <div class="masthead-strip"></div>

    <section class="fee-table">
      <div class="fee-head">
        <div class="fee-head-main">Retainers and Total Estimated Case Costs</div>
        <div class="fee-head-avg">Average Fee<br>Per Case Type</div>
      </div>
      <div class="fee-row"><div class="case-type">Divorce (3301 C): Retainer:</div><div class="retainer">$2,000</div><div class="avg-fee">$1,500 - $3,000</div></div>
      <div class="fee-row"><div class="case-type">Divorce (3301 D): Retainer:</div><div class="retainer">$2,500</div><div class="avg-fee">$2,000 - $3,000</div></div>
      <div class="fee-row"><div class="case-type">Divorce and Custody: Retainer:</div><div class="retainer">$3,500</div><div class="avg-fee">$5,000 - $8,000</div></div>
      <div class="fee-row"><div class="case-type">Divorce and Equitable Distribution: Retainer:</div><div class="retainer">$3,500</div><div class="avg-fee">$6,000 - $10,000</div></div>
      <div class="fee-row"><div class="case-type">Divorce and Support: Retainer:</div><div class="retainer">$3,000</div><div class="avg-fee">$5,000 - $8,000</div></div>
      <div class="fee-row"><div class="case-type">Divorce, Custody and Support: Retainer:</div><div class="retainer">$3,500</div><div class="avg-fee">$8,000 - $12,000</div></div>
      <div class="fee-row"><div class="case-type">Divorce, Equitable Distribution and Support: Retainer:</div><div class="retainer">$3,500</div><div class="avg-fee">$8,000 - $12,000</div></div>
      <div class="fee-row"><div class="case-type">Divorce, Equitable Distribution and Custody: Retainer:</div><div class="retainer">$5,000</div><div class="avg-fee">$10,000 - $15,000</div></div>
      <div class="fee-row"><div class="case-type">Divorce, Equitable Distribution, Custody and Support: Retainer:</div><div class="retainer">$3,500</div><div class="avg-fee">$12,000 - $15,000</div></div>
      <div class="fee-row"><div class="case-type">Custody Initial Order: Retainer:</div><div class="retainer">$3,000</div><div class="avg-fee">$4,000 - $7,000</div></div>
      <div class="fee-row"><div class="case-type">Custody Modification: Retainer:</div><div class="retainer">$3,500</div><div class="avg-fee">$5,000 - $8,000</div></div>
      <div class="fee-row"><div class="case-type">Custody and Support: Retainer:</div><div class="retainer">$3,000</div><div class="avg-fee">$5,000 - $8,000</div></div>
      <div class="fee-row"><div class="case-type">(PFA) Protection From Abuse:</div><div class="retainer">$2,000<br>Paid In Full</div><div class="avg-fee">$1,500 - $3,000</div></div>
    </section>

    <svg class="footer-band" viewBox="0 0 792 30" aria-hidden="true">
      <defs>
        <linearGradient id="footerNavy" x1="0" x2="1" y1="0" y2="0">
          <stop offset="0" stop-color="#12174a"/>
          <stop offset="0.5" stop-color="#24378c"/>
          <stop offset="1" stop-color="#12174a"/>
        </linearGradient>
      </defs>
      <polygon points="0,0 408,0 398,30 0,30" fill="url(#footerNavy)"/>
      <polygon points="408,0 411,0 401,30 398,30" fill="#ffffff"/>
      <polygon points="411,0 792,0 792,30 401,30" fill="#1b4a9e"/>
    </svg>
  </main>
</body>
</html>
```